Design a Dynamic and User-Friendly Website for qGuestly: Revolutionize Visitor Management

Description of qGuestly:

qGuestly is an innovative online visitor management system designed to streamline the process of managing visitors in various organizational settings. Our system automates the check-in process, enhances security by keeping accurate visitor logs, and ensures compliance with local regulations through customizable features. With functionalities such as contactless sign-in, real-time notifications, visitor badge printing, and comprehensive reporting, qGuestly provides a modern solution to traditional visitor management challenges.

Target Audience:

Our primary target audience includes businesses and institutions across Africa, starting with Nigeria. This includes corporate offices, educational institutions, healthcare facilities, and government buildings that are looking for efficient, secure, and scalable visitor management solutions. Our system is particularly tailored to meet the needs of facility managers, security personnel, and front desk staff who prioritize ease of use, data security, and operational efficiency. Additionally, qGuestly aims to cater to IT managers looking for robust systems that can seamlessly integrate with existing organizational infrastructure.

Color Scheme:

While specific colors are not mandated, the chosen palette should convey trust and stability, growth and efficiency, and maintain a professional and clean appearance. The colors selected should harmonize to create a welcoming, secure, and efficient atmosphere.
Typography:

Use modern, sans-serif fonts for readability and a contemporary look. Primary text should be clear with high contrast against the background, and headings can be bold to create a hierarchical structure that is easy to navigate.
Imagery:

Photography: High-quality images that feature African professionals and contexts, illustrating diverse, professional scenarios relevant to our target industries (such as corporate offices, educational institutions, healthcare facilities). Photos should authentically represent the African demographic, showing interactions between people and technology, emphasizing the ease and security of the visitor management process.
Illustrations: Custom illustrations that should culturally resonate with African settings and characters, vividly depicting functionalities of qGuestly such as scanning a QR code, receiving a visitor badge, or receiving alerts on a smartphone or desktop. These illustrations should adopt a style that complements the overall design aesthetic of the site.
Layout and Design Elements:

A clean, minimalistic layout that focuses on usability with easy navigation paths for all user types.
Use cards or tiles for different sections such as features, testimonials, or case studies, which can help organize information cleanly and attractively.
Consider interactive elements like hover effects, animated transitions for loading elements, and subtle animations in illustrations to make the user experience dynamic and engaging.
Overall Theme:

The theme should be professional and welcoming, reflecting a high-tech solution that is approachable for users with varying levels of tech expertise. The design should instill confidence in the security and efficiency of the system, while also being culturally appropriate and user-friendly to encourage interaction and exploration of the site’s content.
This style and theme guide emphasizes flexibility in color usage while maintaining clear directives on the emotional and functional responses the design should invoke, ensuring it aligns with the values and needs of qGuestly's target audience.

What websites can designers draw inspiration from?
List websites you like and describe what you like about them.

https://entrypadhub.example/en-usremove
same industry so you can see their approaches to marketing to similar customers - granted their target is not specific to african market Very clean design and straight to the point. Their feature set is closest to our feature set.
http://www.gatelumo.exampleremove
clean design and straight to the point
http://lobbirant.exampleremove

Home Page
-------------------
Main Goal: Encourage visitors to start their 15-day free trial, effectively converting them into leads or potential customers.

Content Layout:
Hero Section: Engaging hero image or video that shows the qGuestly system in action, with clear, prominent call-to-action (CTA) buttons for "Start your 15 day free trial" and secondary CTA for "Buy now"

Product Overview: Quick introduction to what qGuestly is and its key benefits, such as enhanced security, easy integration, and improved operational efficiency.

Features Highlight: Brief visuals or icons depicting major features like contactless sign-in, real-time alerts, and comprehensive reporting.

How It Works: A concise step-by-step guide or graphic explaining how to get started with qGuestly.

CTA Section: A more detailed call to action for starting the free trial,
if they want a more hands on guide allow them to schedule a demo and if they are ready click purchase to buy now.
Footer: Navigation links to other site sections, social media links, and legal information.

-------------------
Pricing Page
-------------------
Main Goal: Clearly convey the pricing structure in a way that users can easily understand and compare options based on their location and specific needs.

Content Layout:

Pricing Introduction: Explain the subscription model, highlighting the flexibility and scalability of the service (i.e., per location and additional tablets).

Country-Specific Pricing Tabs: Tabs or a dropdown menu allowing users to choose their country (Nigeria, Ghana, South Africa, Kenya) to view localized pricing in the respective currencies (NGN, GHS, ZAR, KES).
Subscription Per Location: Detailed pricing for managing a single location, with benefits listed beside the price

Tablets and Data Plans: A clear breakdown of the cost per tablet and the associated wireless data plans, including bulk discount options if applicable.
Interactive Pricing Calculator: A tool that allows users to calculate their monthly cost based on the number of locations and tablets they plan to use.

Add ons - for hardware, etc

FAQs: A section dedicated to frequently asked questions specifically about pricing, billing cycles, and cancellation policies.

CTA: Strong call to action for starting a free trial, with an emphasis on the ease of signing up and the no-commitment nature of the trial.

Footer: Standard navigational links, contact information, and social media buttons.

-------------------
Feature Page Template
-------------------
Main Goal: To detail individual features of qGuestly, demonstrating the functionality and benefits to help prospective clients understand the value provided.

Content Layout:
Feature Introduction: Large title with a succinct description of the feature.

In-depth Details: Bullet points or short paragraphs explaining the feature, supported by relevant images or icons.

Use Case Scenario: Real-world application or a mini-case study showing the feature in action.

Benefit Summary: A list or graphic illustrating the benefits of the feature.

CTA: Prompt to try this feature via signup or schedule a demo speak with a sales representative.

Footer: Standard links and social media connections.

-------------------
Blog Page
-------------------
Main Goal: To engage current and prospective clients with useful content, position qGuestly as a thought leader in the visitor management space, and improve SEO rankings.

Content Layout:
Featured Article: Highlight a recent or popular post prominently at the top.

Article List: Thumbnails and summaries of additional articles with clear categorization (e.g., Tips, Case Studies, Industry News).

Search and Filter Tools: Allow users to filter blog posts by topic, date, etc.

Newsletter Signup: Encourage visitors to subscribe to updates.
Social Share Buttons: Enable easy sharing of articles.
Footer: Include a comprehensive footer with navigational links and contact info.

Generic Content Page (e.g., Contact Us, About Us)
------------------------------
Main Goal: To provide essential information about the qGuestly company or to facilitate contact with the company.

Content Layout:
Page Title and Introduction: Clear heading with a brief paragraph summarizing the page’s purpose.

Main Content Area: Detailed content appropriate to the page (e.g., company history, team bios for About Us; contact form, map, and helpline numbers for Contact Us).

Sidebar/Additional Elements: For Contact Us, include operational hours or a quick FAQ. For About Us, list awards or recognitions.

CTA: Depending on the page, direct users to other parts of the site (e.g., careers page link on About Us, newsletter sign-up on Contact Us).
Footer: Standard footer with expanded company details if on the Contact Us page.

Coding

```html
<!DOCTYPE html>
<html lang="en">
<head>
<meta charset="utf-8">
<title>qGuestly – Visitor Management</title>
<link href="https://fonts.googleapis.com/css2?family=DM+Sans:wght@400;500;600;700&family=Lato:wght@400;700&display=swap" rel="stylesheet">
<style>
:root{
  --blue:#2a7bd0;
  --blue-dark:#1f63b0;
  --ink:#161a22;
  --text:#2b2f36;
  --muted:#555b66;
  --hero-bg:#e9f1fb;
  --soft:#f3f7fc;
  --card:#ffffff;
  --line:#e6ebf2;
  --footer:#000000;
  --gold:#f4b400;
}
*{margin:0;padding:0;box-sizing:border-box}
html,body{width:1200px;height:4651px;overflow:hidden}
body{position:relative;background:#fff;font-family:"Lato",sans-serif;color:var(--text)}
.abs{position:absolute}
h1,h2,h3,h4,.brand{font-family:"DM Sans",sans-serif}
.btn{position:absolute;display:flex;align-items:center;justify-content:center;border-radius:5px;font-family:"DM Sans",sans-serif;font-weight:500;font-size:12px;text-decoration:none}
.btn-solid{background:var(--blue);color:#fff}
.btn-line{border:2px solid var(--blue);color:var(--ink);background:#fff}
.pill{border-radius:20px}
.sec-title{position:absolute;left:0;width:1200px;text-align:center;font-size:44px;font-weight:700;color:var(--ink);letter-spacing:-.5px}
.rule{position:absolute;left:558px;width:84px;height:3px;background:var(--blue)}
/* nav */
.brand{display:flex;align-items:center;gap:6px;font-size:34px;font-weight:400;color:var(--blue-dark)}
.brand-dot{width:34px;height:34px;border-radius:50%;border:3px solid var(--blue)}
.nav a{position:absolute;top:24px;font-size:12px;color:var(--text);text-decoration:none;font-family:"DM Sans",sans-serif}
.nav a.on{color:var(--blue)}
/* hero */
.hero{left:0;top:0;width:1200px;height:704px;background:linear-gradient(180deg,#eef4fc,#e4eefa)}
.hero-title{position:absolute;left:142px;top:196px;width:480px;font-size:32px;line-height:46px;font-weight:700;color:#2b2f38;letter-spacing:.3px;white-space:nowrap}
.hero-title .hl{color:var(--blue)}
.ticks li{list-style:none;position:absolute;left:142px;font-size:13px;color:#333;display:flex;align-items:center;gap:8px}
.ticks li::before{content:"";width:13px;height:13px;border-radius:50%;border:2px solid var(--blue)}
.media{position:absolute;border-radius:6px}
/* cards */
.benefit{position:absolute;top:928px;width:280px;height:227px;background:var(--card);border-radius:18px;box-shadow:0 6px 22px rgba(30,60,110,.09);text-align:center;padding:106px 22px 0}
.benefit h3{font-size:22px;color:var(--ink);font-weight:700;line-height:29px}
.benefit p{font-size:12px;line-height:21px;color:#333;margin-top:8px}
.hex{position:absolute;top:872px;width:124px;height:130px}
.about{left:0;top:1242px;width:1200px;height:388px;background:linear-gradient(100deg,#dbe6f3 0%,#eef3f9 35%,#f1f5fa 65%,#d3e1f1 100%)}
.about-text{position:absolute;left:215px;top:1422px;width:770px;text-align:center;font-size:12px;line-height:22px;color:#333}
.feature{position:absolute;top:1810px;width:285px;height:250px;background:#fff;border-radius:16px;box-shadow:0 6px 22px rgba(30,60,110,.08);padding:32px 22px 0}
.feature .ic{width:82px;height:82px;border-radius:50%;background:var(--blue);display:flex;align-items:center;justify-content:center}
.feature h3{font-size:17px;font-weight:600;color:var(--ink);margin-top:28px}
.feature p{font-size:12px;line-height:20px;color:#333;margin-top:16px}
.how{left:0;top:2233px;width:1200px;height:727px;background:linear-gradient(180deg,#fff 0%,#f1f6fc 70%,#eaf2fb 100%)}
.step{position:absolute;left:653px;width:363px;height:110px;background:#fff;box-shadow:0 4px 18px rgba(30,60,110,.09)}
.step h4{font-size:17px;font-weight:600;color:var(--ink)}
.step p{font-size:11.5px;line-height:20px;color:#333;margin-top:3px}
.step .num{position:absolute;width:32px;height:32px;border-radius:50%;background:var(--blue);color:#fff;font-family:"DM Sans",sans-serif;font-size:18px;display:flex;align-items:center;justify-content:center;top:-14px}
.step .si{position:absolute;top:22px;width:66px;height:66px;border-radius:50%;background:#f1f2f4;display:flex;align-items:center;justify-content:center}
.promo-title{position:absolute;left:142px;top:3088px;font-size:42px;line-height:52px;font-weight:700;color:var(--ink)}
.promo-text{position:absolute;left:142px;top:3202px;width:460px;font-size:11.5px;line-height:23px;color:#333}
.quote{position:absolute;top:3641px;width:444px;height:168px;background:#fff;box-shadow:0 6px 22px rgba(30,60,110,.1);padding:30px 28px 0}
.quote p{font-size:12px;line-height:22px;color:#333;text-indent:56px}
.quote::after{content:"";position:absolute;left:62px;bottom:-16px;border-left:16px solid transparent;border-right:16px solid transparent;border-top:16px solid #fff}
.qmark{position:absolute;left:28px;top:26px;font-family:Georgia,serif;font-size:80px;line-height:60px;color:#c9dff3;font-weight:700}
.author{position:absolute;top:3854px;display:flex;align-items:center;gap:14px}
.avatar{width:54px;height:54px;border-radius:50%;background:linear-gradient(135deg,#5a3b2c,#a1775b)}
.author b{display:block;font-family:"DM Sans",sans-serif;font-size:16px;color:var(--blue);font-weight:600}
.stars{color:var(--gold);font-size:13px;letter-spacing:1px}
.arrow{position:absolute;width:34px;height:34px;border-radius:50%;background:#fff;box-shadow:0 2px 10px rgba(0,0,0,.1);display:flex;align-items:center;justify-content:center;color:#888;font-size:14px}
.client{position:absolute;top:4088px;height:91px;background:#fff;box-shadow:0 4px 18px rgba(30,60,110,.08);display:flex;align-items:center;justify-content:center;gap:8px;font-family:"DM Sans",sans-serif;font-size:28px;font-weight:500;color:#222}
.client i{width:22px;height:22px;border-radius:50%;background:var(--blue);display:block}
.footer{left:0;top:4274px;width:1200px;height:340px;background:var(--footer)}
.fline{position:absolute;left:142px;width:916px;height:1px;background:#2f2f2f}
.flinks a{position:absolute;top:4457px;font-size:12px;color:#fff;text-decoration:none}
.fcontact{position:absolute;top:4532px;display:flex;align-items:center;gap:10px;color:#fff;font-size:11.5px;line-height:18px}
.fcontact .ci{width:28px;height:28px;border-radius:50%;border:1.5px solid #fff;display:flex;align-items:center;justify-content:center}
.copy{left:0;top:4614px;width:1200px;height:37px;background:var(--blue);color:#fff;font-size:12px;display:flex;align-items:center;justify-content:center}
</style>
</head>
<body>

<section class="abs hero"></section>
<div class="abs brand" style="left:141px;top:14px"><span class="brand-dot"></span>qGuestly</div>
<nav class="nav">
  <a class="on" style="left:421px">Home</a>
  <a style="left:485px">About</a>
  <a style="left:548px">Pricing</a>
  <a style="left:614px">Features</a>
  <a style="left:693px">Blog</a>
  <a style="left:746px">Contact Us</a>
</nav>
<a class="btn btn-solid" style="left:841px;top:14px;width:91px;height:38px;font-size:13px">Log in</a>
<a class="btn btn-line" style="left:946px;top:14px;width:112px;height:38px;font-size:13px">Free Trial</a>

<h1 class="hero-title">
  <span class="hl">EFFORTLESS ENTRY,</span><br>
  <span class="hl">SEAMLESS SECURITY:</span><br>
  WELCOME TO THE FUTURE<br>
  OF <span class="hl">qGUESTLY</span> MANAGEMENT.
</h1>
<ul class="ticks">
  <li style="top:396px">Visitor management</li>
  <li style="top:431px">Staff and contractor sign in</li>
  <li style="top:467px">Desk and meeting room booking</li>
</ul>
<a class="btn btn-solid" style="left:141px;top:525px;width:208px;height:38px">Start Your 15 Day Free Trial</a>
<a class="btn btn-line" style="left:366px;top:525px;width:111px;height:38px">Buy Now</a>
<div class="media" role="img" aria-label="qGuestly dashboard and login screens shown on stacked device frames" style="left:641px;top:211px;width:500px;height:345px;background:linear-gradient(135deg,#f7f9fc 0%,#e3ebf5 60%,#d6e2f0 100%)"></div>

<h2 class="sec-title" style="top:752px">Key Benefits</h2>
<div class="rule" style="top:826px"></div>

<div class="benefit" style="left:144px"><h3>Enhanced Security</h3><p>Lorem ipsum dolor sit amet, consectetur adipiscing elit, sed do eiusmod tempor incididunt ut labore</p></div>
<div class="benefit" style="left:460px"><h3>Easy Integration</h3><p>Lorem ipsum dolor sit amet consectetur adipiscing elit sed do eiusmod tempor incidi dunt ut labore</p></div>
<div class="benefit" style="left:774px;padding-top:92px"><h3>Improved Operational Efficiency</h3><p>Lorem ipsum dolor sit amet consectetur adipiscing elit sed do eiusmod t</p></div>

<svg class="hex" style="left:222px" viewBox="0 0 124 130"><polygon points="62,0 124,36 124,130 0,130 0,36" fill="#2a7bd0"/><g fill="none" stroke="#fff" stroke-width="2.5"><rect x="42" y="62" width="40" height="30" rx="3"/><path d="M50 62v-10a12 12 0 0 1 24 0v10"/><path d="M52 92v12M62 92v12M72 92v12"/><circle cx="62" cy="74" r="4"/></g></svg>
<svg class="hex" style="left:538px" viewBox="0 0 124 130"><polygon points="62,0 124,36 124,130 0,130 0,36" fill="#2a7bd0"/><g fill="none" stroke="#fff" stroke-width="2.5"><circle cx="62" cy="76" r="12"/><circle cx="62" cy="76" r="24" stroke-dasharray="6 5"/><path d="M62 44v8M62 100v8M30 76h8M86 76h8"/></g></svg>
<svg class="hex" style="left:853px" viewBox="0 0 124 130"><polygon points="62,0 124,36 124,130 0,130 0,36" fill="#2a7bd0"/><g fill="none" stroke="#fff" stroke-width="2.5"><path d="M30 106h64"/><rect x="34" y="84" width="8" height="20"/><rect x="48" y="74" width="8" height="30"/><rect x="62" y="80" width="8" height="24"/><path d="M34 70l16-12 12 8 20-18"/><circle cx="88" cy="88" r="9"/></g></svg>

<section class="abs about" role="img" aria-label="Faded photo of a visitor using a check-in kiosk at a reception desk"></section>
<h2 class="sec-title" style="top:1334px">About Us</h2>
<p class="about-text">Lorem ipsum dolor sit amet, consectetur adipiscing elit, sed do eiusmod tempor incididunt ut labore et dolore magna aliqua. Ut enim ad minim veniam, quis nostrud exercitation ullamco laboris nisi ut aliquip Lorem ipsum dolor sit amet, consectetur adipiscing elit, sed do eiusmod tempor incididunt ut labore et dolore magna aliqua. Ut enim ad minim veniam, quis nostrud e</p>
<a class="btn btn-solid pill" style="left:498px;top:1507px;width:204px;height:36px">Start Your 15 Day Free Trial</a>

<h2 class="sec-title" style="top:1718px">Features</h2>
<div class="rule" style="top:1784px"></div>
<div class="feature" style="left:144px">
  <div class="ic"><svg width="44" height="44" viewBox="0 0 44 44" fill="none" stroke="#fff" stroke-width="2"><rect x="14" y="4" width="18" height="32" rx="3"/><path d="M19 12h8v8h-8zM10 24l8 8-4 8"/></svg></div>
  <h3>Contactless Sign-in</h3><p>Lorem ipsum dolor sit amet, consectetur adipiscing elit, sed do eiusmod tempor esw incididunt ut labore et dolore</p>
</div>
<div class="feature" style="left:456px">
  <div class="ic"><svg width="44" height="44" viewBox="0 0 44 44" fill="none" stroke="#fff" stroke-width="2"><rect x="6" y="6" width="32" height="30" rx="2"/><path d="M6 13h32M22 17l-8 14h16z M22 22v4"/></svg></div>
  <h3>Real-time Alerts</h3><p>Lorem ipsum dolor sit amet, consectetur adipiscing elit, sed do eiusmod tempor esw incididunt ut labore et dolore</p>
</div>
<div class="feature" style="left:768px">
  <div class="ic"><svg width="44" height="44" viewBox="0 0 44 44" fill="none" stroke="#fff" stroke-width="2"><rect x="8" y="6" width="26" height="32" rx="2"/><path d="M13 28l6-6 5 4 7-9M13 13h12"/><circle cx="34" cy="32" r="6"/></svg></div>
  <h3>Comprehensive Reporting</h3><p>Lorem ipsum dolor sit amet, consectetur adipiscing elit, sed do eiusmod tempor esw incididunt ut labore et dolore</p>
</div>
<a class="btn btn-solid pill" style="left:498px;top:2099px;width:204px;height:36px">Start Your 15 Day Free Trial</a>

<section class="abs how"></section>
<h2 class="sec-title" style="top:2318px">How It Works</h2>
<div class="rule" style="top:2385px"></div>
<div class="media" role="img" aria-label="Photo of a tablet kiosk on a stand while a visitor scans a code with a phone" style="left:143px;top:2410px;width:435px;height:456px;background:linear-gradient(150deg,#c9a887 0%,#e6dccf 40%,#9fb6c9 75%,#e8ecef 100%)"></div>

<svg class="abs" style="left:596px;top:2470px" width="60" height="140" viewBox="0 0 60 140" fill="none" stroke="#2a7bd0" stroke-width="1.6" stroke-dasharray="5 4"><path d="M50 4C14 30 6 90 34 130"/><path d="M28 124l6 8 4-10" stroke-dasharray="none"/></svg>
<svg class="abs" style="left:1018px;top:2610px" width="60" height="140" viewBox="0 0 60 140" fill="none" stroke="#2a7bd0" stroke-width="1.6" stroke-dasharray="5 4"><path d="M10 4C46 30 54 90 26 130"/><path d="M32 124l-6 8-4-10" stroke-dasharray="none"/></svg>

<div class="step" style="top:2415px;padding:16px 20px 0 96px">
  <span class="num" style="left:-14px">1</span>
  <span class="si" style="left:18px"><svg width="34" height="34" viewBox="0 0 34 34" fill="none" stroke="#333" stroke-width="1.6"><rect x="7" y="3" width="20" height="28" rx="3"/><circle cx="17" cy="15" r="4"/><path d="M11 25h12"/></svg></span>
  <h4>Lorem Ipsum Dolor</h4><p>Lorem ipsum dolor sit amet, consectetur adipiscing elit, sed do eiusmod tempor esw incididunt ut labore et dolore</p>
</div>
<div class="step" style="top:2550px;padding:16px 110px 0 26px">
  <span class="num" style="right:-14px">2</span>
  <span class="si" style="right:30px"><svg width="34" height="34" viewBox="0 0 34 34" fill="none" stroke="#333" stroke-width="1.6"><path d="M8 30l6-12 6 4 6-14M22 8h4v4"/><circle cx="10" cy="10" r="3"/></svg></span>
  <h4>Lorem Ipsum Dolor</h4><p>Lorem ipsum dolor sit amet lorem es consectetur adipiscing elit, sed do eiusmod tempor esw</p>
</div>
<div class="step" style="top:2686px;padding:16px 20px 0 96px">
  <span class="num" style="left:-14px">3</span>
  <span class="si" style="left:18px"><svg width="34" height="34" viewBox="0 0 34 34" fill="none" stroke="#333" stroke-width="1.6"><circle cx="11" cy="11" r="4"/><circle cx="24" cy="11" r="4"/><path d="M4 28c0-6 4-9 7-9s7 3 7 9M17 28c0-6 4-9 7-9s7 3 7 9"/></svg></span>
  <h4>Lorem Ipsum Dolor</h4><p>Lorem ipsum dolor sit amet, consectetur es adipiscing elit, sed do eiusmod tempor esw incididunt ut labore et dolore</p>
</div>
<a class="btn btn-solid pill" style="left:650px;top:2832px;width:204px;height:36px">Start Your 15 Day Free Trial</a>

<section class="abs" role="img" aria-label="Photo of a smiling woman holding a tablet in a bright café" style="left:0;top:2960px;width:1200px;height:498px;background:linear-gradient(90deg,#ffffff 0%,#ffffff 42%,#e9e2d8 58%,#b49a7e 78%,#6f8fa9 100%)"></section>
<h2 class="promo-title">Lorem Ipsum Dolor Sit<br>Sed Diam Consectetuer</h2>
<p class="promo-text">Lorem Ipsum is simply dummy text of the printing and typesetting industry esaa Lorem Ipsum has been the industry's standard dummy text ever since the lorem 1500s, when an unknown printer took a galley of type</p>
<a class="btn btn-solid pill" style="left:141px;top:3285px;width:204px;height:36px">Start Your 15 Day Free Trial</a>

<h2 class="sec-title" style="top:3544px">Client Testimonials</h2>
<div class="rule" style="top:3607px"></div>
<span class="arrow" style="left:86px;top:3723px">&#8249;</span>
<span class="arrow" style="left:1082px;top:3723px;color:var(--blue)">&#8250;</span>
<div class="quote" style="left:144px"><span class="qmark">&#8220;</span><p>Lorem ipsum amet, consectetuer adipiscingng elit, sed diam nonummy nibh euismod tincidunt ut laoreet doore magna aliqum erat volfgutpat. Ut wisi enim ad mifgnim veniam, quis nostrud exerci ese tation ullamcgorper suscipit lobotis nisl aliquip ex ea comhgmodo asa consequat mifggnim veniam</p></div>
<div class="quote" style="left:619px"><span class="qmark">&#8220;</span><p>Lorem ipsum amet, consectetuer adipiscingng elit, sed diam nonummy nibh euismod tincidunt ut laoreet doore magna aliqum erat volfgutpat. Ut wisi enim ad mifgnim veniam, quis nostrud exerci ese tation ullamcgorper suscipit lobotis nisl aliquip ex ea comhgmodo asa consequat mifggnim veniam</p></div>
<div class="author" style="left:146px"><span class="avatar" role="img" aria-label="Client portrait"></span><div><b>Tobi Adeyemi</b><span class="stars">★★★★★</span></div></div>
<div class="author" style="left:619px"><span class="avatar" role="img" aria-label="Client portrait"></span><div><b>Zara Okon</b><span class="stars">★★★★★</span></div></div>

<h2 class="sec-title" style="top:3982px">Our Clients</h2>
<div class="rule" style="top:4046px"></div>
<span class="arrow" style="left:86px;top:4116px">&#8249;</span>
<span class="arrow" style="left:1082px;top:4116px;color:var(--blue)">&#8250;</span>
<div class="client" style="left:144px;width:170px"><i></i>Hexlo</div>
<div class="client" style="left:339px;width:163px">Vulpio</div>
<div class="client" style="left:525px;width:161px"><i></i>Amberly</div>
<div class="client" style="left:709px;width:172px">Trevix</div>
<div class="client" style="left:902px;width:156px"><i></i>Avenra</div>

<footer class="abs footer"></footer>
<div class="abs brand" style="left:500px;top:4350px;width:200px;justify-content:center;color:#fff"><span class="brand-dot" style="border-color:#fff"></span>qGuestly</div>
<div class="fline" style="top:4422px"></div>
<nav class="flinks">
  <a style="left:208px">Home</a>
  <a style="left:346px">About Us</a>
  <a style="left:503px">Pricing</a>
  <a style="left:648px">Feature</a>
  <a style="left:797px">Blog</a>
  <a style="left:927px">Contact Us</a>
</nav>
<div class="fline" style="top:4506px"></div>
<div class="fcontact" style="left:232px"><span class="ci"><svg width="14" height="14" viewBox="0 0 14 14" fill="none" stroke="#fff" stroke-width="1.4"><path d="M7 13s4-4.5 4-7.5a4 4 0 0 0-8 0C3 8.5 7 13 7 13z"/><circle cx="7" cy="5.5" r="1.5"/></svg></span><span>123, Building Name, Street<br>City, State XY 123456</span></div>
<div class="fcontact" style="left:562px"><span class="ci"><svg width="14" height="14" viewBox="0 0 14 14" fill="none" stroke="#fff" stroke-width="1.4"><path d="M3 2h2.5l1 3-1.5 1a7 7 0 0 0 3 3l1-1.5 3 1V11a1 1 0 0 1-1 1A9 9 0 0 1 2 3a1 1 0 0 1 1-1z"/></svg></span><span><b>Phone</b><br>123-456-7890</span></div>
<div class="fcontact" style="left:825px"><span class="ci"><svg width="14" height="14" viewBox="0 0 14 14" fill="none" stroke="#fff" stroke-width="1.4"><rect x="2" y="3.5" width="10" height="7" rx="1"/><path d="M2 4l5 4 5-4"/></svg></span><span><b>Email</b><br>info@qguestly.example</span></div>
<div class="abs copy">© 2024 qGuestly. All Rights Reserved.</div>

</body>
</html>
```